Business Card design for a skin clinic

i would like a business card design for our skin clinic.
our logo colors are Blue and Grey and Bule /white.
we are searching for a minimalistic design yet very elegant,dynamic and professional which can reflect a professional medical skin care clinic( not a beauty salon).
THE DESGIN IS NOT FOR A PERSON IT WILL BE USED IN THE CLINIC FOR CLIENTS SO THERE SHOULD BE NO NAME OF A PERSON ONLY THE CLINIC NAME AND THE CONTACT INFO

Target Market(s)
young and old womens
Industry/Entity Type
Business
Contact Information for Business Card
we have 2 address and both should be on the card.
address A: Lindenhoflaan 214B, 3041KP Rotterdam, Tel 010 483 21 95
address B: Zonnewijzerstraat 238, 1062RT Amsterdam Tel 020 571 3829
website www.huidpuntzorg.nu, email info@huidpuntzorg.nu
Look and feel
Each slider illustrates characteristics of the customer's brand and the style your logo design should communicate.

```html
<!DOCTYPE html>
<html lang="nl">
<head>
<meta charset="utf-8">
<title>Huidpuntzorg – business card</title>
<link rel="stylesheet" href="https://fonts.googleapis.com/css2?family=Jost:wght@300;400;500&display=swap">
<style>
  :root {
    --backdrop: #4a403b;
    --card: #121315;
    --card-edge: #1c1d20;
    --blue: #3a8fd6;
    --grey: #9a9da3;
    --silver: #e4e6ea;
    --ink: #d8dadf;
  }
  * { box-sizing: border-box; margin: 0; padding: 0; }
  html, body { width: 1200px; height: 814px; overflow: hidden; }
  body {
    background: var(--backdrop);
    font-family: "Jost", "Futura", sans-serif;
    display: flex;
    align-items: center;
    justify-content: center;
    gap: 60px;
  }
  .card {
    width: 500px;
    height: 286px;
    background: var(--card);
    border: 1px solid var(--card-edge);
    border-radius: 4px;
    box-shadow: 0 10px 28px rgba(0,0,0,.35);
    position: relative;
  }
  /* contact side */
  .card--contact { padding: 30px 36px; }
  .brand {
    display: flex;
    align-items: center;
    gap: 12px;
  }
  .brand__dot {
    width: 22px; height: 22px;
    border-radius: 50%;
    border: 2px solid var(--blue);
  }
  .brand__name {
    font-weight: 500;
    font-size: 30px;
    letter-spacing: 2px;
    color: var(--blue);
    line-height: 1;
  }
  .tagline {
    font-weight: 300;
    font-size: 12px;
    letter-spacing: 1.5px;
    color: var(--grey);
    margin: 6px 0 0 34px;
  }
  .contact-list {
    list-style: none;
    margin-top: 22px;
    display: grid;
    gap: 6px;
  }
  .contact-list li {
    display: flex;
    align-items: center;
    gap: 10px;
    font-size: 13px;
    font-weight: 400;
    color: var(--ink);
    letter-spacing: .3px;
  }
  .contact-list svg { width: 13px; height: 13px; flex: none; fill: var(--blue); }
  /* logo side */
  .card--logo {
    display: flex;
    flex-direction: column;
    align-items: center;
    justify-content: center;
  }
  .card--logo .brand__dot { width: 30px; height: 30px; border-color: var(--silver); margin-bottom: 18px; }
  .card--logo .brand__name { color: var(--silver); font-size: 36px; letter-spacing: 3px; }
  .card--logo .tagline { margin: 10px 0 0; font-size: 14px; color: var(--silver); }
</style>
</head>
<body>
  <section class="card card--contact">
    <div class="brand">
      <span class="brand__dot"></span>
      <span class="brand__name">HUIDPUNTZORG</span>
    </div>
    <p class="tagline">next generation skin care</p>
    <ul class="contact-list">
      <li><svg viewBox="0 0 24 24"><path d="M12 2a7 7 0 0 0-7 7c0 5 7 13 7 13s7-8 7-13a7 7 0 0 0-7-7zm0 9.5A2.5 2.5 0 1 1 12 6.5a2.5 2.5 0 0 1 0 5z"/></svg>Lindenhoflaan 214B, 3041KP Rotterdam</li>
      <li><svg viewBox="0 0 24 24"><path d="M6.6 10.8a15 15 0 0 0 6.6 6.6l2.2-2.2a1 1 0 0 1 1-.25 11 11 0 0 0 3.6.6 1 1 0 0 1 1 1V20a1 1 0 0 1-1 1A17 17 0 0 1 3 4a1 1 0 0 1 1-1h3.5a1 1 0 0 1 1 1 11 11 0 0 0 .6 3.6 1 1 0 0 1-.25 1z"/></svg>010 483 21 95</li>
      <li><svg viewBox="0 0 24 24"><path d="M12 2a7 7 0 0 0-7 7c0 5 7 13 7 13s7-8 7-13a7 7 0 0 0-7-7zm0 9.5A2.5 2.5 0 1 1 12 6.5a2.5 2.5 0 0 1 0 5z"/></svg>Zonnewijzerstraat 238, 1062RT Amsterdam</li>
      <li><svg viewBox="0 0 24 24"><path d="M6.6 10.8a15 15 0 0 0 6.6 6.6l2.2-2.2a1 1 0 0 1 1-.25 11 11 0 0 0 3.6.6 1 1 0 0 1 1 1V20a1 1 0 0 1-1 1A17 17 0 0 1 3 4a1 1 0 0 1 1-1h3.5a1 1 0 0 1 1 1 11 11 0 0 0 .6 3.6 1 1 0 0 1-.25 1z"/></svg>020 571 3829</li>
      <li><svg viewBox="0 0 24 24"><path d="M3 5h18a1 1 0 0 1 1 1v12a1 1 0 0 1-1 1H3a1 1 0 0 1-1-1V6a1 1 0 0 1 1-1zm1 2.2V17h16V7.2l-8 5.3z M4.5 7l7.5 5 7.5-5z"/></svg>info@huidpuntzorg.nu</li>
      <li><svg viewBox="0 0 24 24"><path d="M12 2a10 10 0 1 0 0 20 10 10 0 0 0 0-20zm7.9 9h-3.4a15 15 0 0 0-1.3-5.7A8 8 0 0 1 19.9 11zM12 4c1 1.3 2.3 3.8 2.5 7h-5C9.7 7.8 11 5.3 12 4zM8.8 5.3A15 15 0 0 0 7.5 11H4.1a8 8 0 0 1 4.7-5.7zM4.1 13h3.4a15 15 0 0 0 1.3 5.7A8 8 0 0 1 4.1 13zM12 20c-1-1.3-2.3-3.8-2.5-7h5c-.2 3.2-1.5 5.7-2.5 7zm3.2-1.3a15 15 0 0 0 1.3-5.7h3.4a8 8 0 0 1-4.7 5.7z"/></svg>www.huidpuntzorg.nu</li>
    </ul>
  </section>

  <section class="card card--logo">
    <span class="brand__dot"></span>
    <span class="brand__name">HUIDPUNTZORG</span>
    <p class="tagline">next generation skin care</p>
  </section>
</body>
</html>
```